High-end construction company needs a business card design

We need a modern looking business card that draws people in, is memorable and looks so good people will want to sick it on their fridges.
On the first side what is needed are:
Logo
My name - Tomas Verbelk
Title - Managing Director
Website - www.kravel.co.uk
Email - tomas@kravel.co.uk
Telephone - 020 5194 6381
Mobile - 07845319027
On the back side was is needed is a list of all the services we provide:
-Kitchen Renovations
-Bathroom Renovations
-House Renovations
-Garage Conversions
-Extensions
-Loft Conversions
-Conservatories
-Carpentry
-Tiling
-Electrical
-Plumbing & Heating
-Bricklaying
-Landscaping
-Decorating
-Plastering
We would like the colours to be the same shades as on the logo with grey or black for the words.
Target Market(s)
Anyone who needs building work done
Contact Information for Business Card
This business card is for a construction company which strives to deliver excellent service and quality.
The look and feel of the card should represent this.
Requirements
Must have
- On the first side what is needed are:
Logo
My name - Tomas Verbelk
Title - Managing Director
Website - www.kravel.co.uk
Email - tomas@kravel.co.uk
Telephone - 020 5194 6381
Mobile - 07845319027
Nice to have
- Cool looking features

```html
<!DOCTYPE html>
<html lang="en">
<head>
<meta charset="utf-8">
<title>Kravel Construction Ltd – Business Card</title>
<link rel="stylesheet" href="https://fonts.googleapis.com/css2?family=Figtree:wght@500;600;700;800&display=swap">
<style>
  :root{
    --stage:#030a22;
    --paper:#ffffff;
    --green:#7ac143;
    --green-dark:#4a9040;
    --ink:#0b1630;
    --wash:#e6f1dd;
    --wash-grey:#e3e8e1;
  }
  *{box-sizing:border-box;margin:0;padding:0}
  html,body{width:1200px;height:1200px;overflow:hidden;background:var(--stage)}
  body{position:relative;font-family:"Figtree",sans-serif;color:var(--ink)}

  .card{position:absolute;left:263px;width:700px;height:400px;background:var(--paper);overflow:hidden}
  .card--front{top:187px}
  .card--back{top:646px}

  .backdrop{position:absolute}
  .card--front .backdrop{left:0;top:0;width:700px;height:384px;
    background:linear-gradient(120deg,rgba(230,241,221,0) 0%,rgba(230,241,221,.9) 40%,rgba(227,232,225,.9) 75%,rgba(230,241,221,.7) 100%);}
  .card--back .backdrop{left:0;top:60px;width:700px;height:324px;
    background:linear-gradient(180deg,rgba(230,241,221,.15) 0%,rgba(230,241,221,.6) 55%,rgba(227,232,225,.7) 100%);}

  .stripes{position:absolute;left:0;bottom:0;width:700px;height:16px}
  .stripes__thick{position:absolute;left:0;top:0;width:100%;height:9px;background:var(--green)}
  .stripes__thin{position:absolute;left:0;bottom:0;width:100%;height:4px;background:var(--green-dark)}

  .brand{position:absolute;color:var(--green);font-weight:800;line-height:1;display:flex;align-items:center;gap:10px}
  .brand__mark{width:14px;height:14px;background:var(--green);flex:none}
  .brand__text{display:flex;flex-direction:column}
  .brand__name{letter-spacing:.02em}
  .brand__sub{letter-spacing:.14em}

  .card--front .brand{left:43px;top:150px}
  .card--front .brand__name{font-size:62px}
  .card--front .brand__sub{font-size:15px;margin-top:6px}

  .divider{position:absolute;left:348px;top:94px;width:3px;height:212px;background:var(--green-dark)}

  .person{position:absolute;left:399px;top:120px;width:250px;text-align:center}
  .person__name{font-size:32px;font-weight:700;letter-spacing:.01em;white-space:nowrap}
  .person__title{font-size:16px;font-weight:700;color:var(--green);margin-top:4px}

  .contacts{position:absolute;left:404px;top:190px;list-style:none;font-size:15.5px;font-weight:600}
  .contacts li{display:flex;align-items:flex-start;height:27px}
  .contacts svg{width:15px;height:15px;margin-right:10px;margin-top:3px;flex:none}
  .contacts .phones{line-height:21px;height:auto}

  .card--back .brand{left:0;width:700px;top:40px;justify-content:center}
  .card--back .brand__name{font-size:54px}
  .card--back .brand__sub{font-size:13px;margin-top:5px}

  .services{position:absolute;left:0;top:170px;width:700px;text-align:center}
  .services__title{font-size:27px;font-weight:700;color:var(--green-dark);margin-bottom:14px}
  .services__row{display:flex;justify-content:center;gap:20px;list-style:none;font-size:16.5px;font-weight:600;height:31px;align-items:center}
  .services__row li::before{content:"";display:inline-block;width:8px;height:8px;border-radius:50%;background:var(--green-dark);margin-right:8px;vertical-align:middle;position:relative;top:-1px}
  .services__web{position:absolute;left:0;width:700px;top:353px;text-align:center;font-size:15px;font-weight:600}
</style>
</head>
<body>

<section class="card card--front">
  <div class="backdrop" role="img" aria-label="Faint illustration of an excavator arm, houses and tall buildings"></div>

  <div class="brand">
    <span class="brand__mark"></span>
    <span class="brand__text">
      <span class="brand__name">KRAVEL</span>
      <span class="brand__sub">CONSTRUCTION LTD</span>
    </span>
  </div>

  <div class="divider"></div>

  <div class="person">
    <h1 class="person__name">TOMAS VERBELK</h1>
    <p class="person__title">MANAGING DIRECTOR</p>
  </div>

  <ul class="contacts">
    <li>
      <svg viewBox="0 0 16 16"><rect x="1" y="3" width="14" height="10" fill="#7ac143"/><path d="M1 3l7 6 7-6M1 13l5-5M15 13l-5-5" stroke="#fff" stroke-width="1.3" fill="none"/></svg>
      tomas@kravel.co.uk
    </li>
    <li>
      <svg viewBox="0 0 16 16" fill="none" stroke="#7ac143" stroke-width="1.3"><circle cx="8" cy="8" r="6.5"/><ellipse cx="8" cy="8" rx="3" ry="6.5"/><path d="M1.5 8h13M2.5 4.8h11M2.5 11.2h11"/></svg>
      www.kravel.co.uk
    </li>
    <li class="phones">
      <svg viewBox="0 0 16 16"><path d="M4 1.5l2.2 2.8-1.3 1.6c.9 2 2.4 3.5 4.3 4.4l1.6-1.3 2.8 2.2-1.4 2.3C7 13.2 2.8 9 2 3z" fill="#7ac143"/></svg>
      <span>07845319027<br>020 5194 6381</span>
    </li>
  </ul>

  <div class="stripes"><div class="stripes__thick"></div><div class="stripes__thin"></div></div>
</section>

<section class="card card--back">
  <div class="backdrop" role="img" aria-label="Faint illustration of houses and tall buildings"></div>

  <div class="brand">
    <span class="brand__mark"></span>
    <span class="brand__text">
      <span class="brand__name">KRAVEL</span>
      <span class="brand__sub">CONSTRUCTION LTD</span>
    </span>
  </div>

  <div class="services">
    <h2 class="services__title">OUR SERVICES</h2>
    <ul class="services__row"><li>Kitchen Renovations</li><li>Bathroom Renovations</li><li>House Renovations</li></ul>
    <ul class="services__row"><li>Garage Conversions</li><li>Extensions</li><li>Loft Conversions</li><li>Conservatories</li></ul>
    <ul class="services__row"><li>Carpentry</li><li>Tiling</li><li>Electrical</li><li>Plumbing &amp; Heating</li><li>Bricklaying</li></ul>
    <ul class="services__row"><li>Landscaping</li><li>Decorating</li><li>Plastering</li></ul>
  </div>

  <p class="services__web">www.kravel.co.uk</p>

  <div class="stripes"><div class="stripes__thick"></div><div class="stripes__thin"></div></div>
</section>

</body>
</html>
```